Brindale transport business cards

Front of card, Looking for my logo on one side of the card

Back of card,
Brindale Transport Maintenance
Onsite Cars, Trucks & trailer maintenance and repairs
Ronan Brindale
0452819036
Brindaletm@fernmail.com

```html
<!DOCTYPE html>
<html lang="en">
<head>
<meta charset="utf-8">
<title>Brindale transport business cards</title>
<link href="https://fonts.googleapis.com/css2?family=Montserrat:wght@400;700&display=swap" rel="stylesheet">
<style>
  :root {
    --page: #ffffff;
    --card: #ffffff;
    --ink: #111111;
    --text: #2b2b2b;
    --blue: #3a78c4;
    --shadow: rgba(0, 0, 0, 0.22);
  }
  * { margin: 0; padding: 0; box-sizing: border-box; }
  html, body {
    width: 1200px;
    height: 1195px;
    overflow: hidden;
    background: var(--page);
    font-family: "Montserrat", sans-serif;
  }
  .sheet {
    position: relative;
    width: 1200px;
    height: 1195px;
  }
  .card {
    position: absolute;
    top: 457px;
    width: 494px;
    height: 281px;
    background: var(--card);
    border-radius: 22px;
    box-shadow: 0 10px 34px var(--shadow);
  }
  .card--front { left: 85px; }
  .card--back { left: 621px; }

  /* front */
  .front-mark {
    position: absolute;
    inset: 0;
    display: flex;
    align-items: center;
    justify-content: center;
    gap: 16px;
  }
  .front-mark__square {
    width: 34px;
    height: 34px;
    background: var(--blue);
  }
  .front-mark__name {
    font-weight: 700;
    font-size: 38px;
    color: var(--ink);
    letter-spacing: 0.5px;
  }

  /* back */
  .back-mark {
    position: absolute;
    left: 36px;
    top: 100px;
    width: 130px;
    display: flex;
    align-items: center;
    gap: 8px;
  }
  .back-mark__square {
    flex: none;
    width: 14px;
    height: 14px;
    background: var(--blue);
  }
  .back-mark__name {
    font-weight: 700;
    font-size: 19px;
    line-height: 1.15;
    color: var(--ink);
  }
  .divider {
    position: absolute;
    left: 176px;
    top: 91px;
    width: 1.5px;
    height: 100px;
    background: var(--blue);
  }
  .contact {
    position: absolute;
    left: 194px;
    top: 96px;
  }
  .contact__name {
    font-weight: 700;
    font-size: 22px;
    color: var(--blue);
    margin-bottom: 20px;
  }
  .contact__line {
    display: flex;
    align-items: center;
    gap: 6px;
    font-size: 13px;
    color: var(--text);
    line-height: 19px;
  }
  .contact__icon { width: 12px; height: 12px; fill: var(--blue); }
  .tagline {
    position: absolute;
    left: 0;
    right: 0;
    top: 228px;
    text-align: center;
    font-size: 13px;
    line-height: 19px;
    color: var(--text);
  }
</style>
</head>
<body>
<main class="sheet">
  <section class="card card--front" aria-label="Card front">
    <div class="front-mark">
      <span class="front-mark__square"></span>
      <span class="front-mark__name">Brindale transport</span>
    </div>
  </section>

  <section class="card card--back" aria-label="Card back">
    <div class="back-mark">
      <span class="back-mark__square"></span>
      <span class="back-mark__name">Brindale transport</span>
    </div>
    <div class="divider"></div>
    <div class="contact">
      <p class="contact__name">Ronan Brindale</p>
      <p class="contact__line">
        <svg class="contact__icon" viewBox="0 0 24 24" aria-hidden="true"><path d="M6.6 10.8a15.1 15.1 0 0 0 6.6 6.6l2.2-2.2a1 1 0 0 1 1-.25 11.4 11.4 0 0 0 3.6.57 1 1 0 0 1 1 1V20a1 1 0 0 1-1 1A17 17 0 0 1 3 4a1 1 0 0 1 1-1h3.5a1 1 0 0 1 1 1c0 1.25.2 2.45.57 3.6a1 1 0 0 1-.25 1z"/></svg>
        0452819036
      </p>
      <p class="contact__line">
        <svg class="contact__icon" viewBox="0 0 24 24" aria-hidden="true"><path d="M2 5h20v14H2z M3.5 6.5 12 13l8.5-6.5" fill="var(--blue)"/><path d="M3 6l9 7 9-7" fill="none" stroke="#fff" stroke-width="1.6"/></svg>
        Brindaletm@fernmail.com
      </p>
    </div>
    <p class="tagline">
      Brindale Transport Maintenance<br>
      Onsite Cars, Trucks &amp; trailer maintenance and repairs
    </p>
  </section>
</main>
</body>
</html>
```